Massage Therapy Business Card

I’d like the same exact business card (same graphics and colors) that I uploaded by R & T Designer with:
Name of the business: Kneadworks by Calder;
Calder Mott (Massage Therapist);
Contact: (555)-418-2730
Email: kneadworksbycalder@mailbox-example.net;
IG: @Gl1de_kneadworks

On the back Please add:
1. Mobile Sessions available upon request
2. Book 3 Massages, Get 4th 50% off

Target Market(s)

Adults ages 21+

Industry/Entity Type

Healthcare and Therapy

Contact Information for Business Card

The color should be different shades of blue with a logo of a male anatomy and pressure points for massages

Colors
0054AA
0677BA
7BADD7
CADEEF
E8F1F8
0094D4
00A9DD
6FCCEA
C7EBF8
E9F6FB
00AB8E
00BBA5
67D7C9
C6EFE9
E9F9F6
EB3D1F
EC4F4E
F09395
F8D3D4
FCEDEE

Requirements
Must have
• Must be Double Sided
Nice to have
• Newer Modern look with a Masculine Feel

```html
<!DOCTYPE html>
<html lang="en">
<head>
<meta charset="utf-8">
<title>Kneadworks by Calder – Business Card</title>
<link rel="stylesheet" href="https://fonts.googleapis.com/css2?family=Poppins:wght@300;400;600;700&display=swap">
<style>
  :root {
    --page: #ececec;
    --blue: #1f52ae;
    --blue-light: #2a74c2;
    --blue-deep: #0f3d93;
    --teal: #35a593;
    --teal-soft: #2e9197;
    --white: #ffffff;
    --ring-white: #e8f1f8;
  }
  * { box-sizing: border-box; margin: 0; padding: 0; }
  html, body { width: 1200px; height: 796px; overflow: hidden; }
  body {
    background: var(--page);
    font-family: "Poppins", sans-serif;
    color: var(--white);
    position: relative;
  }
  .card {
    position: absolute;
    width: 560px;
    height: 320px;
    overflow: hidden;
    border-radius: 4px;
    box-shadow: 0 10px 26px rgba(0,0,0,.22);
  }
  .card--back {
    left: 50px; top: 70px;
    background: linear-gradient(205deg, var(--blue-light) 0%, #2562b6 45%, var(--teal-soft) 100%);
  }
  .card--front {
    left: 590px; top: 406px;
    background: var(--blue);
  }
  .disc { position: absolute; border-radius: 50%; }

  /* back side */
  .card--back .disc--outer { width: 600px; height: 600px; left: -290px; top: -150px; background: var(--blue-deep); }
  .card--back .disc--white { width: 572px; height: 572px; left: -276px; top: -136px; background: var(--ring-white); }
  .card--back .disc--photo {
    width: 550px; height: 550px; left: -265px; top: -125px;
    background: radial-gradient(circle at 75% 60%, #2a5fb3 0%, #2a6cb8 40%, var(--teal-soft) 100%);
  }
  .offers { position: absolute; left: 330px; top: 62px; list-style: none; }
  .offer { position: relative; padding-left: 26px; margin-bottom: 22px; font-size: 13px; line-height: 1.25; font-weight: 300; }
  .offer::before {
    content: ""; position: absolute; left: 0; top: 9px;
    width: 12px; height: 12px; border: 2px solid var(--white); border-radius: 50%;
  }
  .offer strong { font-weight: 600; }

  .brand { position: absolute; font-weight: 700; font-size: 22px; letter-spacing: .5px; line-height: 1; text-transform: uppercase; }
  .card--back .brand { left: 330px; top: 232px; }
  .card--front .brand { left: 40px; top: 262px; }

  /* front side */
  .card--front .disc--outer { width: 460px; height: 460px; left: 290px; top: -150px; background: var(--blue-deep); }
  .card--front .disc--photo {
    width: 430px; height: 430px; left: 318px; top: -146px;
    background: radial-gradient(circle at 40% 65%, var(--teal) 0%, #2f8f9e 45%, #2b6cb8 100%);
  }
  .person { position: absolute; left: 40px; top: 70px; }
  .person__name { font-size: 26px; font-weight: 300; line-height: 1.1; }
  .person__name strong { font-weight: 600; }
  .person__role { font-size: 13px; font-weight: 300; }
  .contacts { position: absolute; left: 40px; top: 150px; list-style: none; font-size: 12.5px; font-weight: 400; }
  .contact { display: flex; align-items: center; gap: 12px; margin-bottom: 9px; }
  .contact svg { width: 16px; height: 16px; flex: none; }
</style>
</head>
<body>

  <section class="card card--back" aria-label="Card back">
    <div class="disc disc--outer"></div>
    <div class="disc disc--white"></div>
    <div class="disc disc--photo" role="img" aria-label="Illustration of a male figure holding his back with a glowing spine and pressure points"></div>
    <ul class="offers">
      <li class="offer"><strong>Mobile Sessions</strong><br>available upon request</li>
      <li class="offer">Book 3 Massages,<br><strong>Get 4th 50% off</strong></li>
    </ul>
    <div class="brand">Kneadworks by Calder</div>
  </section>

  <section class="card card--front" aria-label="Card front">
    <div class="disc disc--outer"></div>
    <div class="disc disc--photo" role="img" aria-label="Illustration of a glowing blue anatomical male figure bending forward with highlighted joints"></div>
    <div class="person">
      <p class="person__name">Calder <strong>Mott</strong></p>
      <p class="person__role">Massage Therapist</p>
    </div>
    <ul class="contacts">
      <li class="contact">
        <svg viewBox="0 0 16 16" aria-hidden="true"><rect x="4" y="1" width="8" height="14" rx="1.5" fill="none" stroke="#fff" stroke-width="1.4"/><line x1="7" y1="12.5" x2="9" y2="12.5" stroke="#fff" stroke-width="1.2"/></svg>
        (555)-418-2730
      </li>
      <li class="contact">
        <svg viewBox="0 0 16 16" aria-hidden="true"><rect x="1" y="3.5" width="14" height="10" rx="1" fill="none" stroke="#fff" stroke-width="1.4"/><polyline points="1.5,4 8,9 14.5,4" fill="none" stroke="#fff" stroke-width="1.4"/></svg>
        kneadworksbycalder@mailbox-example.net
      </li>
      <li class="contact">
        <svg viewBox="0 0 16 16" aria-hidden="true"><circle cx="8" cy="8" r="6" fill="none" stroke="#fff" stroke-width="1.4"/></svg>
        @Gl1de_kneadworks
      </li>
    </ul>
    <div class="brand">Kneadworks by Calder</div>
  </section>

</body>
</html>
```